The Book Cover for "Finding the Silver Lantern of Dawn" needs redesigned

First the back ground or art work needs to be replaced or redesigned.
The title Finding the Silver Lantern of Dawn needs to be redesigned so that the words "Finding the" is diminished in size compared to the rest of the title "Silver Lantern of Dawn"
The Sub-title "Tracing the forgotten path of the Evening Wind" needs to be more pronounced and readable.
The authors name needs to be downsized.

```html
<!DOCTYPE html>
<html lang="en">
<head>
<meta charset="utf-8">
<title>Finding the Silver Lantern of Dawn — Book Cover</title>
<link rel="stylesheet" href="https://fonts.googleapis.com/css2?family=Allura&family=Playfair+Display:wght@500&family=Poppins:wght@400;600;700&display=swap">
<style>
  :root {
    --backdrop: #4b2b5e;
    --sky-violet: #4a2f7a;
    --sky-plum: #8a3f8e;
    --sky-magenta: #b8589a;
    --sky-pink: #e98fae;
    --sky-peach: #f3b08a;
    --sky-orange: #f08a45;
    --sky-ember: #d8471f;
    --ground: #000000;
    --title-coral: #f47f74;
    --kicker-white: #ffffff;
    --script-plum: #3a1838;
    --subtitle-red: #8c2a2e;
    --subtitle-ink: #111111;
    --author-gold: #f2c64c;
  }
  * { margin: 0; padding: 0; box-sizing: border-box; }
  html, body {
    width: 917px;
    height: 1200px;
    overflow: hidden;
    background: var(--backdrop);
  }
  .book-cover {
    position: absolute;
    left: 78px;
    top: 30px;
    width: 760px;
    height: 1140px;
    overflow: hidden;
  }
  .cover-art {
    position: absolute;
    inset: 0;
    background: linear-gradient(180deg,
      var(--sky-violet) 0%,
      var(--sky-plum) 22%,
      var(--sky-magenta) 40%,
      var(--sky-pink) 58%,
      var(--sky-peach) 70%,
      var(--sky-orange) 79%,
      var(--sky-ember) 84%,
      var(--ground) 88%,
      var(--ground) 100%);
  }
  .title-kicker {
    position: absolute;
    left: 64px;
    top: 50px;
    font-family: "Poppins", sans-serif;
    font-weight: 600;
    font-size: 48px;
    line-height: 1;
    color: var(--kicker-white);
    letter-spacing: 0.5px;
    text-transform: uppercase;
  }
  .title-main {
    position: absolute;
    left: 62px;
    font-family: "Playfair Display", serif;
    font-weight: 500;
    font-size: 120px;
    line-height: 1;
    color: var(--title-coral);
    text-transform: uppercase;
    letter-spacing: -1px;
  }
  .title-main--first { top: 90px; }
  .title-main--second { top: 208px; }
  .title-script {
    position: absolute;
    left: 74px;
    top: 292px;
    font-family: "Allura", cursive;
    font-size: 150px;
    line-height: 1;
    color: var(--script-plum);
  }
  .subtitle {
    position: absolute;
    left: 52px;
    top: 676px;
    font-family: "Poppins", sans-serif;
    font-size: 40px;
    line-height: 42px;
    color: var(--subtitle-ink);
  }
  .subtitle-lead {
    font-weight: 700;
    color: var(--subtitle-red);
  }
  .subtitle-rest { font-weight: 400; }
  .author-name {
    position: absolute;
    left: 0;
    right: 0;
    top: 1036px;
    text-align: center;
    font-family: "Poppins", sans-serif;
    font-weight: 700;
    font-size: 34px;
    line-height: 1;
    color: var(--author-gold);
  }
</style>
</head>
<body>
  <main class="book-cover">
    <div class="cover-art" role="img" aria-label="Sunset sky in violet, pink and orange over a grassy field, with the silhouette of a mother lifting a small child into the air"></div>

    <h1 class="book-title">
      <span class="title-kicker">Finding the</span>
      <span class="title-main title-main--first">Silver</span>
      <span class="title-main title-main--second">Lantern</span>
      <span class="title-script">of dawn</span>
    </h1>

    <p class="subtitle">
      <span class="subtitle-lead">Tracing<br>the forgotten</span><br>
      <span class="subtitle-rest">path of the<br>Evening Wind</span>
    </p>

    <p class="author-name">R T Wren Whitcombe</p>
  </main>
</body>
</html>
```